Postcard Design Project

Company Name - Rowan Office Goods LLC We service and Repair printers, Fax and Copiers and sells all Business Technology supplies including supplies for Printers and Copiers to all NYC Metropolitan area.

Target Market(s)

NYC Small to Medium size business

Industry/Entity Type

Business

Font styles to use
Sans Serif

Colors

Designer to choose colors to be used in the design.

Requirements
Must have
• Printer Repairs and Toners Sales

```html
<!DOCTYPE html>
<html lang="en">
<head>
<meta charset="utf-8">
<title>Rowan Office Goods – Printer Repair Postcard</title>
<link rel="stylesheet" href="https://fonts.googleapis.com/css2?family=Barlow+Condensed:wght@600;700&family=Barlow:wght@700;800&family=Lato:wght@700;900&display=swap">
<style>
  :root {
    --canvas: #d9d9d9;
    --card: #fbfaf7;
    --sky-top: #b9dbf2;
    --sky-bottom: #ffffff;
    --brand-blue: #3a6cb0;
    --wave-light: #7cc4ea;
    --sun-yellow: #f6c23c;
    --badge-yellow: #eeec3a;
    --ink: #222222;
    --rule: #9a9a9a;
    --stamp: #333333;
    --photo-light: #c9cdd2;
    --photo-dark: #5b6168;
  }
  * { margin: 0; padding: 0; box-sizing: border-box; }
  html, body { width: 1200px; height: 950px; overflow: hidden; }
  body { position: relative; background: var(--canvas); }

  .postcard {
    position: absolute;
    width: 700px; height: 460px;
    background: var(--card);
    overflow: hidden;
    box-shadow: 0 6px 18px rgba(0,0,0,.2);
  }
  .postcard--front { left: 440px; top: 24px; }
  .postcard--back  { left: 60px;  top: 470px; }
  .postcard__art { position: absolute; inset: 0; }

  /* front */
  .headline {
    position: absolute; left: 46px; top: 14px;
    font-family: "Barlow Condensed", sans-serif; font-weight: 700;
    font-size: 80px; line-height: 1;
    color: var(--brand-blue);
    white-space: nowrap;
    transform: scaleY(1.25); transform-origin: top left;
  }
  .badge-text {
    position: absolute; left: 435px; top: 160px; width: 240px;
    text-align: center;
    font-family: "Barlow Condensed", sans-serif; font-weight: 700;
    font-size: 21px; line-height: 1.02; color: var(--ink);
    text-transform: uppercase;
  }
  .offer {
    position: absolute; left: 26px; top: 220px;
    font-family: "Lato", sans-serif; font-weight: 700;
    font-size: 19px; line-height: 1.25; color: var(--sun-yellow);
    white-space: nowrap;
  }
  .call { position: absolute; left: 26px; top: 300px; }
  .call__label {
    font-family: "Barlow", sans-serif; font-weight: 800;
    font-size: 19px; line-height: 1.1; color: var(--brand-blue); text-transform: uppercase;
  }
  .call__number {
    font-family: "Barlow", sans-serif; font-weight: 800;
    font-size: 54px; line-height: 1; color: var(--brand-blue);
    letter-spacing: -1px; white-space: nowrap;
  }
  .online { position: absolute; left: 26px; top: 384px; }
  .online__label {
    font-family: "Barlow", sans-serif; font-weight: 800;
    font-size: 19px; line-height: 1.1; color: var(--ink); text-transform: uppercase;
  }
  .online__url {
    font-family: "Barlow", sans-serif; font-weight: 800;
    font-size: 25px; line-height: 1.2; color: var(--brand-blue); white-space: nowrap;
  }
  .brand {
    position: absolute;
    display: flex; align-items: center; gap: 8px;
    font-family: "Barlow", sans-serif; font-weight: 800;
    font-size: 18px; color: var(--ink); white-space: nowrap;
  }
  .brand__mark { width: 16px; height: 16px; background: var(--brand-blue); }
  .postcard--front .brand { left: 462px; top: 428px; }

  /* back */
  .back-offer {
    position: absolute; left: 30px; top: 168px;
    font-family: "Lato", sans-serif; font-weight: 900;
    font-size: 20px; line-height: 1.15; color: var(--brand-blue);
    white-space: nowrap;
  }
  .back-call { position: absolute; left: 30px; top: 228px; }
  .back-call .call__label { color: var(--ink); font-size: 16px; }
  .back-call .call__number { color: var(--ink); font-size: 50px; }
  .postcard--back .brand { left: 420px; top: 200px; }
  .back-band-text {
    position: absolute; left: 30px; top: 402px;
    font-family: "Barlow", sans-serif; font-weight: 800;
    font-size: 22px; color: #ffffff; text-transform: uppercase;
    white-space: nowrap; letter-spacing: .5px;
  }
</style>
</head>
<body>

  <section class="postcard postcard--front">
    <svg class="postcard__art" width="700" height="460" viewBox="0 0 700 460">
      <defs>
        <linearGradient id="sky" x1="0" y1="0" x2="0" y2="1">
          <stop offset="0" stop-color="var(--sky-top)"/>
          <stop offset="1" stop-color="var(--sky-bottom)"/>
        </linearGradient>
        <linearGradient id="photo" x1="0" y1="0" x2="1" y2="1">
          <stop offset="0" stop-color="var(--photo-light)"/>
          <stop offset="1" stop-color="var(--photo-dark)"/>
        </linearGradient>
      </defs>
      <rect class="sky" x="0" y="0" width="700" height="200" fill="url(#sky)"/>
      <path class="blue-block" d="M0,180 C130,168 240,210 440,206 L440,290 L0,290 Z" fill="var(--brand-blue)"/>
      <path class="yellow-band" d="M0,290 L450,290 L480,372 L0,372 Z" fill="var(--sun-yellow)"/>
      <path class="wave" d="M0,172 C130,158 240,200 400,196 C540,192 610,160 700,150" fill="none" stroke="var(--wave-light)" stroke-width="16"/>
      <path class="technician-photo" role="img" aria-label="Photo of an opened office printer being repaired with a multimeter"
            d="M420,218 C520,222 610,196 700,180 L700,418 L480,418 Q420,418 420,360 Z"
            fill="url(#photo)" stroke="#555b62" stroke-width="3"/>
      <ellipse class="badge" cx="556" cy="190" rx="128" ry="44" fill="var(--badge-yellow)" stroke="var(--brand-blue)" stroke-width="4"/>
    </svg>

    <h1 class="headline">GOT DIRTY PRINTER?</h1>
    <p class="badge-text">Get a technician<br>in your office<br>today</p>
    <p class="offer">Also check out our unbeatable<br>Ink and Toner online prices</p>
    <div class="call">
      <p class="call__label">Call today:</p>
      <p class="call__number">718-555-0142</p>
    </div>
    <div class="online">
      <p class="online__label">Visit us. online</p>
      <p class="online__url">WWW.ROWANOFFICEGOODS.COM</p>
    </div>
    <div class="brand">
      <span class="brand__mark"></span>
      <span class="brand__name">Rowan Office Goods</span>
    </div>
  </section>

  <section class="postcard postcard--back">
    <svg class="postcard__art" width="700" height="460" viewBox="0 0 700 460">
      <defs>
        <linearGradient id="photo-back" x1="0" y1="0" x2="1" y2="1">
          <stop offset="0" stop-color="var(--photo-light)"/>
          <stop offset="1" stop-color="var(--photo-dark)"/>
        </linearGradient>
      </defs>
      <path class="repair-photo" role="img" aria-label="Photo of a printer's open interior with repair tools"
            d="M0,0 L430,0 L400,80 Q375,150 300,150 L0,150 Z" fill="url(#photo-back)"/>
      <rect class="stamp-box" x="592" y="80" width="72" height="62" fill="var(--stamp)"/>
      <line class="address-line" x1="400" y1="268" x2="664" y2="268" stroke="var(--rule)" stroke-width="1"/>
      <line class="address-line" x1="400" y1="304" x2="664" y2="304" stroke="var(--rule)" stroke-width="1"/>
      <line class="address-line" x1="400" y1="340" x2="664" y2="340" stroke="var(--rule)" stroke-width="1"/>
      <rect class="yellow-rule" x="0" y="376" width="700" height="4" fill="var(--sun-yellow)"/>
      <rect class="blue-band" x="0" y="380" width="700" height="80" fill="var(--brand-blue)"/>
    </svg>

    <p class="back-offer">Also check out our unbeatable<br>Ink and Toner online prices</p>
    <div class="back-call">
      <p class="call__label">Call today:</p>
      <p class="call__number">718-555-0142</p>
    </div>
    <div class="brand">
      <span class="brand__mark"></span>
      <span class="brand__name">Rowan Office Goods</span>
    </div>
    <p class="back-band-text">Visit us. online : www.rowanofficegoods.com</p>
  </section>

</body>
</html>
```